Bright Lanterns Business Card

Design of business cards

Target Market(s)

We are aiming as small business owners who need anything from basic business structures, website plans, business processes and quality assurance.

Industry/Entity Type

Business

Colors

Designer to choose colors to be used in the design.

Requirements
Nice to have
• I would prefer one side of the card to use the green from the logo. Prefer to have the same font as the logo.

```html
<!DOCTYPE html>
<html lang="en">
<head>
<meta charset="utf-8">
<title>Bright Lanterns Business Card Options</title>
<link href="https://fonts.googleapis.com/css2?family=Cinzel:wght@400;600&family=Open+Sans:wght@400&display=swap" rel="stylesheet">
<style>
  :root {
    --lantern-green: #a6ce39;
    --charcoal: #58585a;
    --paper: #f5f6f5;
    --white: #ffffff;
    --card-edge: #c9c9c9;
    --ink: #111111;
  }
  * { box-sizing: border-box; margin: 0; padding: 0; }
  html, body {
    width: 1200px; height: 764px; overflow: hidden;
    background: var(--white);
  }
  .sheet { position: relative; width: 1200px; height: 764px; }

  .option-label {
    position: absolute;
    font-family: "Open Sans", Arial, sans-serif;
    font-size: 46px; line-height: 1;
    color: var(--ink);
  }

  .card {
    position: absolute;
    width: 503px; height: 334px;
    border: 1.5px solid var(--card-edge);
    background: var(--lantern-green);
    overflow: hidden;
    font-family: "Cinzel", "Times New Roman", serif;
  }
  .card-header {
    height: 108px;
    background: var(--paper);
    border-bottom: 5px solid var(--charcoal);
    display: flex; align-items: center; justify-content: center; gap: 14px;
  }
  .brand-dot {
    width: 18px; height: 18px; border-radius: 50%;
    background: var(--lantern-green);
  }
  .brand-name {
    font-weight: 600; font-size: 22px; letter-spacing: 0.5px;
    color: var(--lantern-green);
  }

  .holder-name {
    position: absolute; left: 0; right: 0; top: 182px;
    text-align: center;
    font-size: 39px; font-weight: 400; letter-spacing: 1px;
    line-height: 1;
  }
  .holder-name.is-charcoal { color: var(--charcoal); }
  .holder-name.is-white { color: var(--white); }

  .contact-row {
    position: absolute; left: 18px; right: 18px; top: 291px;
    display: flex; justify-content: space-between; align-items: center;
    color: var(--white); font-size: 15px;
  }
  .contact-item { display: flex; align-items: center; gap: 6px; }
  .contact-item svg { width: 22px; height: 22px; }

  .phone-centered {
    position: absolute; left: 0; right: 0; top: 246px;
    display: flex; justify-content: center; align-items: center; gap: 10px;
    color: var(--charcoal); font-size: 27px;
  }
  .phone-centered svg { width: 34px; height: 34px; }

  .phone-icon circle { fill: none; stroke: currentColor; stroke-width: 1.6; }
  .phone-icon path { fill: currentColor; }
</style>
</head>
<body>
<main class="sheet">

  <!-- Option A -->
  <span class="option-label" style="left:22px; top:30px;">a</span>
  <section class="card" style="left:62px; top:36px;">
    <header class="card-header">
      <span class="brand-dot"></span>
      <span class="brand-name">Bright Lanterns Consulting</span>
    </header>
    <h1 class="holder-name is-charcoal">Marcus Ellery</h1>
    <div class="contact-row">
      <span class="contact-item">
        <svg class="phone-icon" viewBox="0 0 24 24"><circle cx="12" cy="12" r="10.5"/><path d="M8.2 6.5l2 2.1-1.1 1.6c.7 1.6 2 2.9 3.6 3.7l1.6-1.1 2.1 2-1.2 1.8c-3.8-.5-7.3-4-7.8-7.8z"/></svg>
        000-111-222
      </span>
      <span class="contact-item">www.(yourwebsite).com</span>
    </div>
  </section>

  <!-- Option B -->
  <span class="option-label" style="left:626px; top:30px;">b</span>
  <section class="card" style="left:666px; top:36px;">
    <header class="card-header">
      <span class="brand-dot"></span>
      <span class="brand-name">Bright Lanterns Consulting</span>
    </header>
    <h1 class="holder-name is-white">Marcus Ellery</h1>
    <div class="contact-row">
      <span class="contact-item">
        <svg class="phone-icon" viewBox="0 0 24 24"><circle cx="12" cy="12" r="10.5"/><path d="M8.2 6.5l2 2.1-1.1 1.6c.7 1.6 2 2.9 3.6 3.7l1.6-1.1 2.1 2-1.2 1.8c-3.8-.5-7.3-4-7.8-7.8z"/></svg>
        000-111-222
      </span>
      <span class="contact-item">www.(yourwebsite).com</span>
    </div>
  </section>

  <!-- Option C -->
  <span class="option-label" style="left:22px; top:391px;">c</span>
  <section class="card" style="left:62px; top:397px;">
    <header class="card-header">
      <span class="brand-dot"></span>
      <span class="brand-name">Bright Lanterns Consulting</span>
    </header>
    <h1 class="holder-name is-white">Marcus Ellery</h1>
    <div class="phone-centered">
      <svg class="phone-icon" viewBox="0 0 24 24"><circle cx="12" cy="12" r="10.5"/><path d="M8.2 6.5l2 2.1-1.1 1.6c.7 1.6 2 2.9 3.6 3.7l1.6-1.1 2.1 2-1.2 1.8c-3.8-.5-7.3-4-7.8-7.8z"/></svg>
      000-111-222
    </div>
  </section>

  <!-- Option D -->
  <span class="option-label" style="left:626px; top:391px;">d</span>
  <section class="card" style="left:666px; top:397px;">
    <header class="card-header">
      <span class="brand-dot"></span>
      <span class="brand-name">Bright Lanterns Consulting</span>
    </header>
    <h1 class="holder-name is-charcoal">Marcus Ellery</h1>
    <div class="phone-centered">
      <svg class="phone-icon" viewBox="0 0 24 24"><circle cx="12" cy="12" r="10.5"/><path d="M8.2 6.5l2 2.1-1.1 1.6c.7 1.6 2 2.9 3.6 3.7l1.6-1.1 2.1 2-1.2 1.8c-3.8-.5-7.3-4-7.8-7.8z"/></svg>
      000-111-222
    </div>
  </section>

</main>
</body>
</html>
```